Laser hair removal, Cellulite Reduction PDT Led Light Therapy & Hot Stone Massage

I need a business card design for a new business based in Sydney Australia. Our treatments include Laser Hair Removal, Cellulite & Fat Reduction,
PDT LED light rejuvenation therapy, and Hot Stone Massage. The main Medical Aesthetician has a Nursing background of 12yrs and is also a Registered Nurse .All treatments are safe painless and effective using the latest Technology.
It is located at 4/17 Marlow Terrace, Kendrick Vale NSW Mbl: 0431 607 519
Watch for our Specials

Target Market(s)

Male & Females

Industry/Entity Type

Business

Contact Information for Business Card

Body Treatments from Head to toe

Colors
33b8a4
86cfc6
00a990
a64599
b868aa
d3a5cc

Requirements
Must have
• All my Treatments on the card and a nice call to attention statement
• Must be colourful in Blue or Green hues
Nice to have
• A nice image of a male & female together
Should not have
• Should not look overcrowded with words

```html
<!DOCTYPE html>
<html lang="en">
<head>
<meta charset="utf-8">
<title>Stillwater Body Care – Business Card</title>
<link rel="stylesheet" href="https://fonts.googleapis.com/css2?family=Philosopher:wght@400;700&family=Fondamento&display=swap">
<style>
  :root {
    --canvas: #ececec;
    --card: #f7f7f7;
    --band-deep: #6b6bff;
    --band-light: #9d9dff;
    --band-mid-deep: #7070dc;
    --band-mid-light: #9c9cff;
    --teal: #10a38b;
    --violet: #6a6aec;
    --heading: #6565d2;
    --white: #ffffff;
  }
  * { margin: 0; padding: 0; box-sizing: border-box; }
  html, body { width: 1200px; height: 1000px; overflow: hidden; }
  body {
    background: var(--canvas);
    position: relative;
    font-family: "Philosopher", sans-serif;
  }
  .card {
    position: absolute;
    width: 654px;
    height: 351px;
    background: var(--card);
    overflow: hidden;
  }
  .card--front { left: 104px; top: 104px; }
  .card--back  { left: 454px; top: 533px; }

  .band {
    position: absolute;
    left: 0; right: 0;
    background: linear-gradient(100deg, var(--band-deep) 0%, var(--band-light) 22%, var(--band-deep) 45%, var(--band-light) 75%, var(--band-deep) 100%);
  }
  .band--top { top: 0; height: 35px; }
  .band--bottom { bottom: 0; height: 40px; }

  /* front */
  .brand {
    position: absolute;
    top: 80px; left: 0; right: 0;
    text-align: center;
    font-size: 46px;
    font-weight: 400;
    color: var(--teal);
    letter-spacing: 0.5px;
    line-height: 1;
  }
  .contact {
    position: absolute;
    top: 198px; left: 0; right: 0;
    list-style: none;
    text-align: center;
    color: var(--violet);
    font-size: 17px;
    line-height: 29px;
  }
  .contact li { display: flex; justify-content: center; align-items: center; gap: 7px; }
  .contact svg { fill: var(--violet); }

  /* back */
  .treatments-title {
    position: absolute;
    top: 64px; left: 0; right: 0;
    text-align: center;
    font-size: 27px;
    font-weight: 400;
    color: var(--heading);
    letter-spacing: 0.5px;
  }
  .treatments {
    position: absolute;
    top: 117px; left: 0; right: 0; height: 116px;
    background: linear-gradient(110deg, var(--band-mid-deep) 0%, var(--band-mid-light) 30%, #8b8bf0 60%, var(--band-mid-light) 80%, var(--band-mid-deep) 100%);
    list-style: none;
    text-align: center;
    color: var(--white);
    font-size: 20px;
    line-height: 25px;
    padding-top: 7px;
  }
  .callout {
    position: absolute;
    top: 250px; left: 0; right: 0;
    text-align: center;
    font-family: "Fondamento", cursive;
    font-size: 36px;
    color: var(--teal);
  }
</style>
</head>
<body>

<section class="card card--front" aria-label="Card front">
  <div class="band band--top"></div>
  <h1 class="brand">Stillwater Body Care</h1>
  <ul class="contact">
    <li>
      <svg width="12" height="13" viewBox="0 0 24 24" aria-hidden="true"><path d="M6.6 10.8a15 15 0 0 0 6.6 6.6l2.2-2.2c.3-.3.7-.4 1-.2 1.1.4 2.3.6 3.6.6.6 0 1 .4 1 1V20c0 .6-.4 1-1 1A17 17 0 0 1 3 4c0-.6.4-1 1-1h3.5c.6 0 1 .4 1 1 0 1.3.2 2.5.6 3.6.1.3 0 .7-.2 1z"/></svg>
      <span>0431 607 519</span>
    </li>
    <li>
      <svg width="20" height="13" viewBox="0 0 24 16" aria-hidden="true"><path d="M1 0h22c.6 0 1 .4 1 1v.5L12 8 0 1.5V1c0-.6.4-1 1-1zM0 3.8l12 6.5 12-6.5V15c0 .6-.4 1-1 1H1c-.6 0-1-.4-1-1z"/></svg>
      <span>hello@stillwaterbody.net</span>
    </li>
    <li>
      <svg width="18" height="16" viewBox="0 0 24 22" aria-hidden="true"><path d="M12 0 0 10.5h3.5V22h6.5v-7h4v7h6.5V10.5H24z"/></svg>
      <span>4/17 Marlow Terrace, Kendrick Vale NSW</span>
    </li>
  </ul>
  <div class="band band--bottom"></div>
</section>

<section class="card card--back" aria-label="Card back">
  <div class="band band--top"></div>
  <h2 class="treatments-title">Our Treatments:</h2>
  <ul class="treatments">
    <li>Laser Hair Removal</li>
    <li>Cellulite &amp; Fat Reduction</li>
    <li>PDT LED Light Rejuvenation Therapy</li>
    <li>Hot Stone Massage</li>
  </ul>
  <p class="callout">Watch for Our Specials</p>
  <div class="band band--bottom"></div>
</section>

</body>
</html>
```